MLR showcase

"We're looking for an event poster for a blues music genre "Riverbend Revue" event. Overall feel should be like a vintage concert poster. Consider use of textures / weathering masks, and if photos are (optionally) used, consider posterizing the photos.
Attached is an example concept poster as well as sponsor's logo. All of the text from the concept poster, as well as sponsor's logo, should be used in the new design.
Photos of the three artists involved may *optionally* be used and can be downloaded, if desired, from:
http://marshlanternrecords.com/presskits/mabel/photos/
http://marshlanternrecords.com/presskits/ruth/photos/
http://marshlanternrecords.com/presskits/arnoldpratt/photos/
Final image should be 8.5x11, 300 dpi, but should be legible when reduced to 1/4 of that size for printing 4-up on a 8.5x11 page (or "postcard" size).
Deliverable should include layered Photoshop and/or Illustrator source files, and identification of all fonts used.

```html
<!DOCTYPE html>
<html lang="en">
<head>
<meta charset="utf-8">
<title>Riverbend Revue</title>
<link href="https://fonts.googleapis.com/css2?family=Alfa+Slab+One&family=Oswald:wght@500;600&display=swap" rel="stylesheet">
<style>
  :root {
    --yellow: #e6e36b;
    --yellow-deep: #d6cf4c;
    --paper: #ebe8df;
    --paper-edge: #d8d4c7;
    --teal: #2b6e86;
    --teal-dark: #225a6e;
    --ink: #3b3a37;
  }
  html, body { margin: 0; padding: 0; overflow: hidden; }
  body { width: 927px; height: 1200px; }
  .poster {
    position: relative; width: 927px; height: 1200px; overflow: hidden;
    background: radial-gradient(circle at 50% 50%, var(--yellow) 55%, var(--yellow-deep) 100%);
  }
  .artwork { position: absolute; inset: 0; }
  .title { font-family: "Alfa Slab One", serif; fill: var(--teal); }
  .line { font-family: "Oswald", sans-serif; font-weight: 500; fill: var(--ink); }
  .tagline { font-family: "Oswald", sans-serif; font-weight: 500; fill: var(--ink); font-size: 21px; }
  .label-name { font-family: "Oswald", sans-serif; font-weight: 500; fill: var(--teal); }
  .url { font-family: "Oswald", sans-serif; font-weight: 600; fill: var(--ink); font-size: 30px; }
  .star-teal { fill: var(--teal); }
  .star-ink { fill: var(--ink); }
</style>
</head>
<body>
<main class="poster">
  <svg class="artwork" width="927" height="1200" viewBox="0 0 927 1200">
    <defs>
      <radialGradient id="paper-tone" cx="50%" cy="40%" r="70%">
        <stop offset="60%" stop-color="#ebe8df"/>
        <stop offset="100%" stop-color="#d8d4c7"/>
      </radialGradient>
      <linearGradient id="artist-tone" x1="0" y1="0" x2="0" y2="1">
        <stop offset="0" stop-color="#2b6e86"/>
        <stop offset="1" stop-color="#225a6e"/>
      </linearGradient>
      <symbol id="star" viewBox="0 0 24 24"><polygon points="12,1 15,9 23.5,9 16.7,14.2 19.3,22.5 12,17.4 4.7,22.5 7.3,14.2 0.5,9 9,9"/></symbol>
    </defs>

    <rect class="sheet" x="38" y="33" width="851" height="1134" fill="url(#paper-tone)"/>

    <!-- Headline -->
    <text class="title" x="91" y="265" font-size="200" textLength="788" lengthAdjust="spacingAndGlyphs">RIVERBEND</text>
    <text class="title" x="94" y="397" font-size="112" textLength="400" lengthAdjust="spacingAndGlyphs">REVUE</text>

    <!-- Date -->
    <text class="line" x="545" y="379" font-size="52" textLength="168" lengthAdjust="spacingAndGlyphs">THU MAY 8</text>
    <use href="#star" class="star-teal" x="722" y="344" width="32" height="32"/>
    <text class="line" x="762" y="379" font-size="52" textLength="86" lengthAdjust="spacingAndGlyphs">FREE</text>

    <!-- Act 1 -->
    <text class="line" x="83" y="508" font-size="66" textLength="134" lengthAdjust="spacingAndGlyphs">12:45</text>
    <use href="#star" class="star-teal" x="228" y="470" width="30" height="30"/>
    <text class="line" x="265" y="508" font-size="66" textLength="299" lengthAdjust="spacingAndGlyphs">ARNOLD PRATT</text>
    <use href="#star" class="star-teal" x="603" y="420" width="48" height="48"/>
    <use href="#star" class="star-teal" x="672" y="420" width="48" height="48"/>
    <use href="#star" class="star-teal" x="741" y="420" width="48" height="48"/>
    <text class="tagline" x="83" y="538" textLength="334" lengthAdjust="spacingAndGlyphs">AS SEEN ON “BACKROADS”</text>

    <!-- Act 2 -->
    <use href="#star" class="star-teal" x="79" y="586" width="40" height="40"/>
    <use href="#star" class="star-teal" x="131" y="586" width="40" height="40"/>
    <use href="#star" class="star-teal" x="183" y="586" width="40" height="40"/>
    <use href="#star" class="star-teal" x="235" y="586" width="40" height="40"/>
    <use href="#star" class="star-teal" x="287" y="586" width="40" height="40"/>
    <text class="line" x="341" y="603" font-size="66" textLength="99" lengthAdjust="spacingAndGlyphs">1:45</text>
    <use href="#star" class="star-teal" x="456" y="566" width="30" height="30"/>
    <text class="line" x="500" y="603" font-size="66" textLength="348" lengthAdjust="spacingAndGlyphs">MABEL HART</text>
    <text class="tagline" x="311" y="632" textLength="276" lengthAdjust="spacingAndGlyphs">“INTELLIGENTLY SEXY</text>
    <use href="#star" class="star-ink" x="593" y="615" width="17" height="17"/>
    <text class="tagline" x="616" y="632" textLength="225" lengthAdjust="spacingAndGlyphs">SLYLY SUBVERSIVE”</text>

    <!-- Act 3 -->
    <text class="line" x="86" y="724" font-size="66" textLength="111" lengthAdjust="spacingAndGlyphs">2:45</text>
    <use href="#star" class="star-teal" x="210" y="686" width="30" height="30"/>
    <text class="line" x="255" y="724" font-size="66" textLength="263" lengthAdjust="spacingAndGlyphs">RUTH BELL</text>
    <use href="#star" class="star-teal" x="556" y="654" width="48" height="48"/>
    <use href="#star" class="star-teal" x="629" y="654" width="48" height="48"/>
    <use href="#star" class="star-teal" x="702" y="654" width="48" height="48"/>
    <text class="tagline" x="94" y="753" textLength="194" lengthAdjust="spacingAndGlyphs">“LITTLE BOOGALOO”</text>

    <!-- Venue -->
    <text class="line" x="530" y="830" font-size="80" textLength="318" lengthAdjust="spacingAndGlyphs">DALTON’S</text>
    <text class="line" x="530" y="924" font-size="80" textLength="303" lengthAdjust="spacingAndGlyphs">218 FRONT</text>

    <!-- Artists -->
    <path class="artists" role="img" aria-label="Posterized teal photo of the three performing artists"
          d="M15 1200 V860 Q15 790 90 780 L420 780 Q500 790 500 860 V1200 Z" fill="url(#artist-tone)"/>

    <!-- Presenter -->
    <text class="line" x="700" y="988" font-size="19" textLength="91" lengthAdjust="spacingAndGlyphs">PRESENTED BY</text>
    <text class="label-name" x="560" y="1048" font-size="42" textLength="300" lengthAdjust="spacingAndGlyphs">MARSH LANTERN</text>
    <text class="label-name" x="640" y="1088" font-size="32" textLength="140" lengthAdjust="spacingAndGlyphs">RECORDS</text>
    <text class="url" x="553" y="1143" textLength="323" lengthAdjust="spacingAndGlyphs">marshlanternrecords.com</text>
  </svg>
</main>
</body>
</html>
```